Signage for a store*

logo on the two sides of the sign
in the middle is the name of the store witch is VORELT
at the bottom of the two logos, one side for location/address and the other side is contact details phone number is 718-392-6107 address is 2974 THE SIGN WILL BEE 15 FEET BY 4 FEET I WOULD LIKE THAT THE
BACKGROUND OF THE SIGN SHOULD HAVE A NICE COLOR BASE
THAT GOES FOR A WINE STORE

```html
<!DOCTYPE html>
<html lang="en">
<head>
<meta charset="utf-8">
<title>VORELT — Store Sign</title>
<link rel="stylesheet" href="https://fonts.googleapis.com/css2?family=Zilla+Slab:wght@400;500&family=Montserrat:wght@400;500&display=swap">
<style>
  :root {
    --wine-bg: #260913;
    --crimson: #b3264e;
    --gold: #c9a45a;
    --gold-faint: rgba(201, 164, 90, 0.14);
  }
  * { margin: 0; padding: 0; box-sizing: border-box; }
  html, body { width: 1200px; height: 319px; overflow: hidden; background: var(--wine-bg); }
  .sign {
    position: relative;
    width: 1200px;
    height: 319px;
    background: var(--wine-bg);
    font-family: "Montserrat", sans-serif;
    color: var(--gold);
  }
  .corner-ornament {
    position: absolute;
    top: 0;
    width: 150px;
    height: 110px;
  }
  .corner-ornament--left {
    left: 0;
    background: radial-gradient(circle at 0 0, var(--gold-faint) 0%, rgba(201,164,90,0.06) 55%, transparent 75%);
  }
  .corner-ornament--right {
    right: 0;
    width: 190px;
    background: radial-gradient(circle at 100% 0, var(--gold-faint) 0%, rgba(201,164,90,0.06) 55%, transparent 75%);
  }
  .brand-mark {
    position: absolute;
    top: 28px;
    width: 110px;
    display: flex;
    flex-direction: column;
    align-items: center;
    gap: 12px;
  }
  .brand-mark--left { left: 16px; }
  .brand-mark--right { left: 1006px; }
  .brand-mark__dot {
    width: 84px;
    height: 84px;
    border-radius: 50%;
    background: var(--crimson);
  }
  .brand-mark__name {
    font-family: "Zilla Slab", serif;
    font-weight: 500;
    font-size: 26px;
    letter-spacing: 1px;
    color: var(--gold);
  }
  .store-title {
    position: absolute;
    top: 98px;
    left: 0;
    width: 1200px;
    display: flex;
    justify-content: center;
    align-items: center;
    gap: 34px;
  }
  .store-title__name {
    font-family: "Zilla Slab", serif;
    font-weight: 400;
    font-size: 96px;
    line-height: 1;
    letter-spacing: 4px;
    color: var(--crimson);
  }
  .store-title__meta {
    font-family: "Zilla Slab", serif;
    font-size: 17px;
    letter-spacing: 2px;
    color: var(--gold);
    padding-bottom: 6px;
    border-bottom: 1px solid var(--gold);
    margin-top: 12px;
  }
  .contact {
    position: absolute;
    top: 258px;
    display: flex;
    align-items: center;
    gap: 12px;
    font-size: 22px;
    color: var(--gold);
  }
  .contact--phone { left: 26px; }
  .contact--address { right: 26px; }
  .contact svg { width: 28px; height: 28px; }
</style>
</head>
<body>
  <main class="sign">
    <div class="corner-ornament corner-ornament--left" role="img" aria-label="Faint gold leaf ornament in the top left corner"></div>
    <div class="corner-ornament corner-ornament--right" role="img" aria-label="Faint gold leaf ornament in the top right corner"></div>

    <div class="brand-mark brand-mark--left">
      <span class="brand-mark__dot"></span>
      <span class="brand-mark__name">VORELT</span>
    </div>
    <div class="brand-mark brand-mark--right">
      <span class="brand-mark__dot"></span>
      <span class="brand-mark__name">VORELT</span>
    </div>

    <h1 class="store-title">
      <span class="store-title__meta">ESTD</span>
      <span class="store-title__name">VORELT</span>
      <span class="store-title__meta">2019</span>
    </h1>

    <div class="contact contact--phone">
      <svg viewBox="0 0 24 24" fill="none" stroke="currentColor" stroke-width="1.5" aria-hidden="true">
        <circle cx="12" cy="12" r="11"/>
        <path d="M8.2 6.5l1.9-.3 1.1 2.6-1.3 1a7 7 0 0 0 3.3 3.3l1-1.3 2.6 1.1-.3 1.9c-4.6.6-8.9-3.7-8.3-8.3z"/>
      </svg>
      <span>718-392-6107</span>
    </div>

    <div class="contact contact--address">
      <svg viewBox="0 0 24 24" fill="none" stroke="currentColor" stroke-width="1.5" aria-hidden="true">
        <circle cx="12" cy="12" r="11"/>
        <path d="M12 18.5s-4.2-4.4-4.2-7.4a4.2 4.2 0 0 1 8.4 0c0 3-4.2 7.4-4.2 7.4z"/>
        <circle cx="12" cy="11" r="1.5"/>
      </svg>
      <span>2974</span>
    </div>
  </main>
</body>
</html>
```